AI Business Tools Landing Page

My web-based website builder (Brindora.com) will be adding many new features in the very near future and I need an eye-catching landing page to promote these new products.

The page will have a primary section of the 8 main products we are promoting:
1. AI Instant Website Generator
2. AI Chatbot
3. Online Store Builder with AI Assistance
4. AI Auto-Blogging System
5. Online Scheduling System
6. Custom Email System
7. SEO Service
8. CRM System

The page will also have a smaller section for links to our affiliate programs. These can be smaller, less-promanent buttons or links. These are the affiliate products:
1. Get Your LLC
2. Website Design and Maintenance
3. Vorlo Ads Management
4. Social Media Posting Service
5. Logo Design
6. Trademark Registration
7. Patent Application
8. Printing Services (including postcards, flyers, and merch.)
9. Bulk AI Content Generator

The theme and color scheme of the page should follow the theme of our main website, which is https://brindora.com.

I need the page fully coded and ready to deploy on my server.

I look forward to seeing your amazing designs!

```html
<!DOCTYPE html>
<html lang="en">
<head>
<meta charset="utf-8">
<title>Brindora – The Premier AI Website Builder</title>
<link href="https://fonts.googleapis.com/css2?family=Lexend:wght@300;400;500;600&family=Poppins:wght@400;500;600&display=swap" rel="stylesheet">
<style>
:root{
  --navy:#0b1f44;
  --navy-deep:#081733;
  --ink:#0f1f3d;
  --text:#4a5468;
  --blue:#2b8ef2;
  --blue-soft:#4fb0ff;
  --sky:#eaf4fd;
  --sky-2:#d6eafb;
  --mint:#7fd6aa;
  --white:#ffffff;
}
*{box-sizing:border-box;margin:0;padding:0}
html,body{width:1200px;height:5386px;overflow:hidden}
body{position:relative;background:var(--white);font-family:"Poppins",sans-serif;color:var(--ink)}
.abs{position:absolute}

/* Hero */
.hero{position:absolute;left:0;top:0;width:1200px;height:640px;background:linear-gradient(160deg,#071a3d 0%,#0c2c66 55%,#1763c4 100%);overflow:hidden}
.hero__art{position:absolute;left:420px;top:0;width:780px;height:600px;background:radial-gradient(ellipse at 65% 35%,rgba(120,190,255,.55),rgba(40,110,220,.25) 45%,transparent 70%),radial-gradient(ellipse at 30% 85%,rgba(80,200,255,.45),transparent 55%)}
.brand{position:absolute;display:flex;align-items:center;gap:12px;font-family:"Lexend",sans-serif;font-weight:500;color:var(--white)}
.brand__mark{width:30px;height:30px;border-radius:50%;background:var(--blue-soft)}
.hero .brand{left:108px;top:28px;font-size:34px}
.btn-mint{position:absolute;display:flex;align-items:center;justify-content:center;background:var(--mint);color:var(--white);border-radius:20px;font-family:"Lexend",sans-serif;font-weight:500;font-size:11.5px}
.hero__cta-top{left:905px;top:32px;width:188px;height:36px}
.hero__title{position:absolute;left:108px;top:170px;font-family:"Lexend",sans-serif;font-weight:600;font-size:48px;line-height:68px;color:var(--white)}
.hero__btn{position:absolute;left:108px;top:330px;width:186px;height:34px;border-radius:18px;background:var(--blue);color:var(--white);font-family:"Lexend",sans-serif;font-size:11.5px;font-weight:500;display:flex;align-items:center;justify-content:center}
.hero__wave{position:absolute;left:0;top:440px}

.band-light{position:absolute;left:0;top:600px;width:1200px;height:460px;background:linear-gradient(180deg,#f5faff 0%,#e6f2fd 100%)}

/* Features */
.feature{position:absolute;width:520px}
.feature__title{font-family:"Lexend",sans-serif;font-weight:500;font-size:38px;line-height:50px;color:var(--ink)}
.feature__title mark{background:linear-gradient(180deg,transparent 52%,var(--blue) 52%, var(--blue) 92%,transparent 92%);color:var(--ink)}
.feature__rail{position:absolute;left:36px;width:250px;border-top:1.5px solid var(--blue);border-left:1.5px solid var(--blue)}
.feature__rail::before{content:"";position:absolute;right:0;top:-18px;height:18px;border-right:1.5px solid var(--blue)}
.feature__rail::after{content:"";position:absolute;left:-6px;bottom:0;width:9px;height:9px;border-right:1.5px solid var(--blue);border-bottom:1.5px solid var(--blue);transform:rotate(45deg)}
.feature__list{list-style:none;margin:24px 0 0 90px;width:400px}
.feature__list li{position:relative;padding-left:22px;font-size:11.5px;line-height:18px;color:var(--text);margin-bottom:20px}
.feature__list li::before{content:"";position:absolute;left:2px;top:3px;width:10px;height:5px;border-left:2px solid var(--blue);border-bottom:2px solid var(--blue);transform:rotate(-45deg)}
.art{position:absolute;border-radius:40px}

/* Resources */
.band-sky{position:absolute;left:0;top:4020px;width:1200px;height:1000px;background:linear-gradient(180deg,#e9f3fd 0%,#f7fbff 55%,#eaf3fc 100%)}
.res__mark{position:absolute;left:556px;top:4080px;width:86px;height:86px;border-radius:50%;background:var(--blue-soft)}
.res__frame{position:absolute;left:104px;top:4235px;width:992px;height:285px;border:1.5px solid var(--blue);border-top:none}
.res__frame::before,.res__frame::after{content:"";position:absolute;top:0;border-top:1.5px solid var(--blue);width:100px}
.res__frame::before{left:0}.res__frame::after{right:0}
.res__title{position:absolute;left:0;top:4215px;width:1200px;text-align:center;font-family:"Lexend",sans-serif;font-weight:400;font-size:38px;line-height:46px;color:var(--ink)}
.res__row{position:absolute;left:0;width:1200px;display:flex;justify-content:center;gap:12px}
.pill{height:34px;padding:0 22px;border:1.5px solid #9ccff7;border-radius:4px;background:var(--white);color:var(--blue);font-family:"Lexend",sans-serif;font-size:11.5px;font-weight:500;display:flex;align-items:center}
.pill--active{background:var(--blue);color:var(--white);border-color:var(--blue)}
.res__cta{left:486px;top:4502px;width:228px;height:34px}

/* Testimonials */
.reviews__title{position:absolute;left:0;top:4625px;width:1200px;text-align:center;font-family:"Lexend",sans-serif;font-weight:500;font-size:38px;color:var(--ink)}
.reviews__sub{position:absolute;left:0;top:4685px;width:1200px;text-align:center;font-size:13px;color:var(--ink)}
.card{position:absolute;top:4722px;width:385px;height:168px;background:var(--white);border-radius:8px;box-shadow:0 6px 16px rgba(20,60,120,.14);padding:22px 22px 0 82px}
.card__quote{position:absolute;left:18px;top:22px;width:46px;height:46px;border-radius:50%;background:var(--blue);color:var(--white);font-family:"Lexend",sans-serif;font-size:30px;line-height:56px;text-align:center}
.card__name{font-family:"Lexend",sans-serif;font-weight:600;font-size:12px}
.card__role{font-size:9px;color:var(--text);margin-top:6px}
.card__stars{color:#ef4b3d;font-size:14px;letter-spacing:2px;margin:8px 0}
.card__text{font-size:8.5px;line-height:14px;color:var(--text)}
.card__text b{color:var(--ink);font-weight:600}

/* Footer */
.footer{position:absolute;left:0;top:4960px;width:1200px;height:426px}
.footer .brand{left:454px;top:120px;font-size:44px}
.footer .brand__mark{width:68px;height:68px}
.footer__text{position:absolute;left:0;top:246px;width:1200px;text-align:center;font-size:13px;line-height:19px;color:var(--white)}
.social{position:absolute;left:0;top:306px;width:1200px;display:flex;justify-content:center;gap:12px}
.social span{width:22px;height:22px;border-radius:50%;border:1.2px solid #5f86c4}
.footer__copy{position:absolute;left:0;top:358px;width:1200px;text-align:center;font-size:10px;color:#c8d6ee}
.footer__copy b{color:var(--blue-soft);font-weight:500}
</style>
</head>
<body>

<header class="hero">
  <div class="hero__art" role="img" aria-label="Glowing wireframe robotic hand touching a digital circuit surface"></div>
  <div class="brand"><span class="brand__mark"></span>Brindora</div>
  <a class="btn-mint hero__cta-top">Get started for free!</a>
  <h1 class="hero__title">The Premier<br>AI Website Builder</h1>
  <a class="hero__btn">Build my free website</a>
  <svg class="hero__wave" width="1200" height="200" viewBox="0 0 1200 200">
    <path d="M0 40 C300 150 650 40 900 140 C1020 185 1120 170 1200 150 L1200 200 L0 200Z" fill="#f5faff"/>
    <path d="M460 150 C700 40 880 120 1000 170 C1080 195 1150 180 1200 160" fill="none" stroke="#2b8ef2" stroke-width="5"/>
  </svg>
</header>

<div class="band-light"></div>
<svg class="abs" style="left:0;top:980px" width="1200" height="120" viewBox="0 0 1200 120"><path d="M0 40 C300 10 500 90 800 70 C1000 55 1100 20 1200 30 L1200 120 L0 120Z" fill="#fff"/></svg>

<!-- 1 -->
<section class="feature" style="left:108px;top:705px">
  <h2 class="feature__title">AI Instant <mark>Website</mark><br><mark>Generator</mark></h2>
  <div class="feature__rail" style="top:90px;height:148px"></div>
  <ul class="feature__list">
    <li>Get a professional, seo-optimized website in seconds!</li>
    <li>Includes custom domain, secure high-speed hosting, professional images, and more!</li>
  </ul>
</section>
<div class="art" style="left:625px;top:690px;width:465px;height:290px;background:radial-gradient(ellipse at 50% 55%,#c9d8ff,#efe6ff 60%,transparent 75%)" role="img" aria-label="Robot beside a computer monitor with gears and plants"></div>

<!-- 2 -->
<div class="art" style="left:110px;top:1160px;width:390px;height:290px;background:radial-gradient(ellipse at 45% 55%,#9fd0ff,#ffe3d6 60%,transparent 75%)" role="img" aria-label="Chatbot in a phone greeting a customer"></div>
<section class="feature" style="left:612px;top:1185px">
  <h2 class="feature__title">AI <mark>Chatbot</mark></h2>
  <div class="feature__rail" style="top:42px;height:172px;width:120px"></div>
  <ul class="feature__list" style="margin-top:30px">
    <li>Fully-Trainable chatbot will learn about your business to automate the customer support process!</li>
    <li>Built-in crm features integrate emailing, text messaging, and contact forms!</li>
  </ul>
</section>

<!-- 3 -->
<section class="feature" style="left:108px;top:1565px">
  <h2 class="feature__title">Online Store Builder<br>(E-Commerce) <mark>With AI</mark><br><mark>Assistance</mark></h2>
  <div class="feature__rail" style="top:140px;height:142px"></div>
  <ul class="feature__list">
    <li>Sell you products online and integrate your products into any website!</li>
    <li>Accept payments from multiple payment gateways including Payverly and Quidrop!</li>
  </ul>
</section>
<div class="art" style="left:690px;top:1520px;width:405px;height:380px;background:radial-gradient(ellipse at 55% 50%,#b8d8ff,#e6eefc 60%,transparent 75%)" role="img" aria-label="Shoppers booking products on a large laptop with a robot assistant"></div>

<!-- 4 -->
<div class="art" style="left:105px;top:1940px;width:395px;height:380px;background:radial-gradient(ellipse at 50% 55%,#9fe3e6,#e6e2fb 60%,transparent 75%)" role="img" aria-label="Laptop surrounded by blog article cards"></div>
<section class="feature" style="left:612px;top:2010px">
  <h2 class="feature__title">AI <mark>Auto-Blogging</mark><br><mark>System</mark></h2>
  <div class="feature__rail" style="top:90px;height:160px;width:160px"></div>
  <ul class="feature__list">
    <li>AI will generate an incredible blog for your business in seconds and immediately begin posting content for you!</li>
    <li>Choose from daily, weekly, or monthly automated blog posting, consistent, unique, seo-optimized content posting on cruise control!</li>
  </ul>
</section>

<!-- 5 -->
<section class="feature" style="left:108px;top:2395px">
  <h2 class="feature__title">Online <mark>Scheduling</mark><br><mark>System</mark></h2>
  <div class="feature__rail" style="top:90px;height:150px;width:250px"></div>
  <ul class="feature__list">
    <li>Get Appointment Bookings, Restaurant Reservations, Or Consultations Scheduled Directly From Your Website!</li>
    <li>Manage Your Employees' Schedules And All Your Appointments From A Simple, User-Friendly Dashboard!</li>
  </ul>
</section>
<div class="art" style="left:700px;top:2390px;width:395px;height:250px;background:radial-gradient(ellipse at 50% 50%,#bcd6ff,#ffe1d3 60%,transparent 75%)" role="img" aria-label="Person marking a wall calendar beside a clock"></div>

<!-- 6 -->
<div class="art" style="left:100px;top:2710px;width:400px;height:300px;background:radial-gradient(ellipse at 50% 55%,#b9c7ff,#e8ecff 60%,transparent 75%)" role="img" aria-label="Large envelope on a phone with people working on laptops"></div>
<section class="feature" style="left:612px;top:2740px">
  <h2 class="feature__title">Custom Emails<br><mark>Using Your Domain</mark></h2>
  <div class="feature__rail" style="top:90px;height:160px;width:140px"></div>
  <ul class="feature__list">
    <li>Quickly set up emails for yourself and all your employees with your own domain extension (example - johnd@yoursite.com), no more unprofessional Maildrift and Yonderpost email addresses!</li>
    <li>Manage all your business emails from a simple, user-friendly interface!</li>
  </ul>
</section>

<!-- 7 -->
<section class="feature" style="left:108px;top:3095px">
  <h2 class="feature__title">SEO Service –<br>Automatic <mark>Backlink</mark><br><mark>Building</mark></h2>
  <div class="feature__rail" style="top:140px;height:220px;width:170px"></div>
  <ul class="feature__list">
    <li>Let us do the hard work of getting high-quality backlinks to your website. although difficult to get, backlinks to your website boost search engine ranking more than any other strategy!</li>
    <li>Subscribe now and start getting 10-20 high-quality permanent backlinks to your website every month, guaranteed!</li>
  </ul>
</section>
<div class="art" style="left:700px;top:3095px;width:395px;height:335px;background:radial-gradient(ellipse at 50% 50%,#9cc3f5,#e3eefc 60%,transparent 75%)" role="img" aria-label="Large SEO lettering surrounded by gears and a keyboard"></div>

<!-- 8 -->
<div class="art" style="left:100px;top:3530px;width:420px;height:350px;background:radial-gradient(ellipse at 50% 50%,#a9d4ff,#e5f1ff 60%,transparent 75%)" role="img" aria-label="Isometric CRM dashboard with charts and cards"></div>
<section class="feature" style="left:612px;top:3590px">
  <h2 class="feature__title">CRM <mark>System</mark></h2>
  <div class="feature__rail" style="top:42px;height:162px;width:90px"></div>
  <ul class="feature__list" style="margin-top:30px">
    <li>Automate the lead follow up process to consistently stay in front of your potential customers!</li>
    <li>Schedule automatic email and text campaigns and effortlessly follow your funnels from lead to closing!</li>
  </ul>
</section>

<a class="btn-mint" style="left:507px;top:3884px;width:186px;height:36px">Get started for free!</a>

<!-- Resources -->
<div class="band-sky"></div>
<svg class="abs" style="left:0;top:3990px" width="1200" height="80" viewBox="0 0 1200 80"><path d="M0 40 C300 10 600 70 900 40 C1050 25 1150 30 1200 35 L1200 0 L0 0Z" fill="#fff"/></svg>
<div class="res__mark"></div>
<div class="res__frame"></div>
<h2 class="res__title">Additional resources to help launch<br>your business</h2>
<div class="res__row" style="top:4356px">
  <a class="pill">Get Your LLC</a>
  <a class="pill pill--active">Website Design And Maintenance</a>
  <a class="pill">Vorlo Ads Management</a>
  <a class="pill">Social Media Posting Service</a>
</div>
<div class="res__row" style="top:4406px">
  <a class="pill">Logo Design</a>
  <a class="pill">Trademark Registration</a>
  <a class="pill">Patent Application</a>
  <a class="pill">Printing Services</a>
  <a class="pill">Bulk AI Content Generator</a>
</div>
<a class="btn-mint res__cta">Explore Our Affiliate Programs</a>

<!-- Reviews -->
<h2 class="reviews__title">What our site owners says</h2>
<p class="reviews__sub">Read testimonials from happy brindora customers!</p>
<article class="card" style="left:202px">
  <span class="card__quote">“</span>
  <div class="card__name">Noah R.</div>
  <div class="card__role">Tech Start-Up Founder</div>
  <div class="card__stars">★★★★★</div>
  <p class="card__text">In the tech world, having an impressive website is essential. Brindora delivered beyond my expectations. <b>It's not just a website builder ; it's a business game-changer.</b></p>
</article>
<article class="card" style="left:613px">
  <span class="card__quote">“</span>
  <div class="card__name">Maya K.</div>
  <div class="card__role">Food Blogger</div>
  <div class="card__stars">★★★★★</div>
  <p class="card__text">Starting my food blog has never been easier. Brindora's templates are gorgeous, and the site was up and running in no time. <b>I'm in Love With How Everything Turned Out!</b></p>
</article>

<!-- Footer -->
<footer class="footer">
  <svg class="abs" style="left:0;top:0" width="1200" height="426" viewBox="0 0 1200 426">
    <path d="M0 40 C250 0 450 70 700 45 C900 25 1050 20 1200 40 L1200 426 L0 426Z" fill="#0b1f44"/>
  </svg>
  <div class="brand"><span class="brand__mark"></span>Brindora</div>
  <p class="footer__text">It'll take minutes or less! just answer a few basic questions and watch your<br>stunning new website generate in seconds!</p>
  <div class="social"><span></span><span></span><span></span><span></span><span></span><span></span><span></span><span></span><span></span></div>
  <p class="footer__copy">© 2024 <b>Brindora</b>. All Rights Reserved</p>
</footer>

</body>
</html>
```